Manufacturing company needs new business card.

I need a unique Business Card that will truly stand out. Nothing too busy. Simple is good, right? Not looking for a standard design either. No cookie cutter layout. I am just looking for something interesting and a bit different. Does't have to completely off the wall crazy, just not your run of the mill business card. Clean and modern with a touch of industrial.

Target Market(s)

Air conditioning industry, Architects, builders.

Industry/Entity Type

Business

Contact Information for Business Card

Details to be included on card are:

Peter Vance
Managing Director

T: 1300 847 519
M: 0428 593 174
W: www.brenvaleworks.com.au
E: peter.vance@brenvaleworks.com.au
A: 58 Harwick Lane, Sydney NSW 2000

Font styles to use
Sans Serif

Colors
0355a3
848484
fbfbfb

Requirements
Must have
• Card design must be landscape.

```html
<!DOCTYPE html>
<html lang="en">
<head>
<meta charset="utf-8">
<title>Brenvale Works – Business Card</title>
<link href="https://fonts.googleapis.com/css2?family=Lato:wght@400;700&display=swap" rel="stylesheet">
<style>
  :root{
    --brand-blue:#2352a8;
    --brand-grey:#848484;
    --paper:#fbfbfb;
    --ink:#555a66;
    --stage:#2b2b2d;
  }
  *{margin:0;padding:0;box-sizing:border-box}
  html,body{width:1200px;height:880px;overflow:hidden}
  body{background:var(--stage);font-family:'Lato',sans-serif;position:relative}

  .card{position:absolute;width:560px;height:320px;border-radius:18px;overflow:hidden}

  /* Front */
  .card--front{left:60px;top:80px;background:var(--brand-blue)}
  .wordmark{position:absolute;display:flex;align-items:center;gap:18px;color:#fff}
  .wordmark__square{width:44px;height:44px;background:#fff;border-radius:4px;flex:none}
  .wordmark__text{display:flex;flex-direction:column}
  .wordmark__name{font-size:46px;font-weight:400;line-height:1;letter-spacing:.5px}
  .wordmark__sub{display:flex;align-items:center;gap:10px;margin-top:6px}
  .wordmark__rule{height:2px;background:#fff;flex:1}
  .wordmark__country{font-size:15px;letter-spacing:9px}
  .card--front .wordmark{left:88px;top:118px}

  /* Back */
  .card--back{left:580px;top:480px;background:var(--paper)}
  .back__band{position:absolute;left:0;top:0;width:100%;height:150px;background:var(--brand-blue)}
  .back__stripe{position:absolute;left:0;top:150px;width:100%;height:9px;background:var(--brand-grey)}
  .card--back .wordmark{left:40px;top:62px}
  .card--back .wordmark__name{font-size:36px}
  .card--back .wordmark__country{font-size:13px;letter-spacing:8px}
  .holder{position:absolute;right:34px;top:30px;color:#fff;text-align:right}
  .holder__name{font-size:18px;font-weight:700;letter-spacing:.5px;text-transform:uppercase}
  .holder__title{font-size:13px;margin-top:2px}

  .contacts{position:absolute;left:40px;bottom:30px;list-style:none}
  .contacts li{display:flex;align-items:center;gap:10px;font-size:14px;color:var(--ink);height:23px}
  .contacts .icon{width:18px;height:18px;border-radius:4px;background:var(--brand-blue);display:flex;align-items:center;justify-content:center;flex:none}
  .contacts svg{width:12px;height:12px;fill:none;stroke:#fff;stroke-width:1.6;stroke-linecap:round;stroke-linejoin:round}
</style>
</head>
<body>

<section class="card card--front" aria-label="Card front">
  <div class="wordmark">
    <span class="wordmark__square"></span>
    <div class="wordmark__text">
      <span class="wordmark__name">Brenvale Works</span>
      <div class="wordmark__sub"><span class="wordmark__rule"></span><span class="wordmark__country">AUSTRALIA</span></div>
    </div>
  </div>
</section>

<section class="card card--back" aria-label="Card back">
  <div class="back__band"></div>
  <div class="back__stripe"></div>

  <div class="wordmark">
    <div class="wordmark__text">
      <span class="wordmark__name">Brenvale Works</span>
      <div class="wordmark__sub"><span class="wordmark__rule"></span><span class="wordmark__country">AUSTRALIA</span></div>
    </div>
  </div>

  <div class="holder">
    <div class="holder__name">Peter Vance</div>
    <div class="holder__title">Managing Director</div>
  </div>

  <ul class="contacts">
    <li><span class="icon"><svg viewBox="0 0 12 12"><path d="M3 1.5l1.5 2.2-1 1a6 6 0 003.8 3.8l1-1 2.2 1.5-.8 1.5C5.5 10.5 1.5 6.5 1.5 2.3z"/></svg></span>1300 847 519</li>
    <li><span class="icon"><svg viewBox="0 0 12 12"><rect x="3.5" y="1" width="5" height="10" rx="1"/><path d="M5.5 9h1"/></svg></span>0428 593 174</li>
    <li><span class="icon"><svg viewBox="0 0 12 12"><rect x="1" y="2.5" width="10" height="7" rx="1"/><path d="M1 3l5 4 5-4"/></svg></span>peter.vance@brenvaleworks.com.au</li>
    <li><span class="icon"><svg viewBox="0 0 12 12"><circle cx="6" cy="6" r="5"/><path d="M1 6h10M6 1c-2.5 3-2.5 7 0 10M6 1c2.5 3 2.5 7 0 10"/></svg></span>www.brenvaleworks.com.au</li>
    <li><span class="icon"><svg viewBox="0 0 12 12"><path d="M6 11S2 7 2 4.5a4 4 0 018 0C10 7 6 11 6 11z"/><circle cx="6" cy="4.5" r="1.3"/></svg></span>58 Harwick Lane, Sydney NSW 2000</li>
  </ul>
</section>

</body>
</html>
```